Business Card Design

I need a Business Card that will catch the attention that will not get thrown in a Drawer. I have 23 companies I use for Auto, Home, Life, and Business Insurance. I make sure that people have the best coverage for the $ spent.

Industry/Entity Type

Business

Contact Information for Business Card

Dorlin Insurance Agency, Inc., Marcus Helgren, 4375 West Tamber Lane Larkfield, Westmark 45192 555-281-7496, www.dorlinagency.example, Friendnet, Worklink, Circleplus

```html
<!DOCTYPE html>
<html lang="en">
<head>
<meta charset="utf-8">
<title>Dorlin Insurance Agency — Business Cards</title>
<link rel="stylesheet" href="https://fonts.googleapis.com/css2?family=Cinzel:wght@400&family=Dosis:wght@600;700&display=swap">
<style>
  :root {
    --backdrop: #e9e6e2;
    --card: #ffffff;
    --band: #3b3431;
    --brown: #8b4a1f;
    --band-text: #e8e3df;
  }
  * { box-sizing: border-box; margin: 0; padding: 0; }
  html, body {
    width: 1200px; height: 900px; overflow: hidden;
    background: var(--backdrop);
  }
  .canvas {
    position: relative; width: 1200px; height: 900px;
    display: flex; flex-direction: column; align-items: center; justify-content: center; gap: 44px;
  }
  .card {
    position: relative; width: 700px; height: 400px;
    background: var(--card);
    box-shadow: 0 6px 18px rgba(0,0,0,0.18);
    overflow: hidden;
  }
  .top-band {
    position: absolute; left: 0; top: 0; width: 100%; height: 74px;
    background: var(--band);
    display: flex; align-items: center; justify-content: flex-end; padding-right: 34px;
  }
  .agency-name {
    font-family: "Cinzel", serif; font-weight: 400; font-size: 25px;
    letter-spacing: 1px; color: var(--band-text);
  }
  .bottom-band {
    position: absolute; left: 0; bottom: 0; width: 100%; height: 56px;
    background: var(--band);
    display: flex; align-items: center; padding-left: 30px; gap: 60px;
    font-family: "Dosis", sans-serif; font-weight: 700; color: var(--band-text);
    font-size: 21px; letter-spacing: 1px;
  }
  .person {
    position: absolute;
    font-family: "Dosis", sans-serif; color: var(--brown); text-transform: uppercase;
  }
  .person-name { font-weight: 700; font-size: 44px; letter-spacing: 1px; line-height: 1; }
  .person-address { font-weight: 600; font-size: 21px; letter-spacing: 1px; line-height: 1.3; margin-top: 14px; }
  .social {
    position: absolute; right: 30px; bottom: 68px;
    display: flex; gap: 12px; list-style: none;
    font-family: "Dosis", sans-serif; font-weight: 700; font-size: 13px;
    color: var(--band); text-transform: uppercase; letter-spacing: 0.5px;
  }
  .social-item { display: flex; align-items: center; gap: 4px; }
  .social-item::before {
    content: ""; width: 10px; height: 10px; background: var(--brown);
  }

  /* Agency name in the mark position */
  .agency-mark {
    position: absolute;
    display: flex; align-items: center;
    font-family: "Dosis", sans-serif; font-weight: 700; color: var(--band);
    text-transform: uppercase; letter-spacing: 2px;
  }
  .agency-mark::before { content: ""; background: var(--band); }

  .card--boxed .agency-mark { left: 42px; top: 170px; font-size: 34px; gap: 12px; }
  .card--boxed .agency-mark::before { width: 30px; height: 30px; }
  .card--boxed .person { left: 262px; top: 122px; }

  .card--centered .agency-mark { left: 300px; top: 92px; font-size: 18px; gap: 8px; }
  .card--centered .agency-mark::before { width: 16px; height: 16px; }
  .card--centered .person { left: 220px; top: 136px; }
</style>
</head>
<body>
<main class="canvas">
  <article class="card card--boxed">
    <header class="top-band"><span class="agency-name">Dorlin Insurance Agency, Inc.</span></header>
    <div class="agency-mark">Dorlin</div>
    <section class="person">
      <h1 class="person-name">Marcus Helgren</h1>
      <p class="person-address">4375 West Tamber Lane<br>Larkfield, Westmark 45192</p>
    </section>
    <ul class="social">
      <li class="social-item">Friendnet</li>
      <li class="social-item">Worklink</li>
      <li class="social-item">Circleplus</li>
    </ul>
    <footer class="bottom-band">
      <span class="phone">555-281-7496</span>
      <span class="website">WWW.DORLINAGENCY.EXAMPLE</span>
    </footer>
  </article>

  <article class="card card--centered">
    <header class="top-band"><span class="agency-name">Dorlin Insurance Agency, Inc.</span></header>
    <div class="agency-mark">Dorlin</div>
    <section class="person">
      <h1 class="person-name">Marcus Helgren</h1>
      <p class="person-address">4375 West Tamber Lane<br>Larkfield, Westmark 45192</p>
    </section>
    <ul class="social">
      <li class="social-item">Friendnet</li>
      <li class="social-item">Worklink</li>
      <li class="social-item">Circleplus</li>
    </ul>
    <footer class="bottom-band">
      <span class="phone">555-281-7496</span>
      <span class="website">WWW.DORLINAGENCY.EXAMPLE</span>
    </footer>
  </article>
</main>
</body>
</html>
```